Stationery Design Project - Mark Delouris

I have recently designed my personal logo - Mark Delouris (here on briefhivo.net) and now i'm looking to complete my corporate identity, with adding:
- Business Card
- Letter Head
- Envelope
- Brochure template (that will be used to promote any of the workshops or other services I provide along with a short summary about my credentials, and testimonials) - you can take your pick from the website: http://markdelouris.net

Refer to website for more insight into the brand and the look & feel

PS.
- PLEASE REFER TO ATTACHED FILE AND READ THE "SHOULD NOT HAVE SECTION OF THIS BRIEF"
- I have attached two vector files, displaying the logo alteration on two different backgrounds (dark & light)

ONLY 2 DAYS LEFT ON DEADLINE. KEEP THOSE DESIGNS COMING.

Target Market(s)

1) One-on-one Business Executive 2) Companies requesting my workshops for mid management teams & public speaking events like KIP Forums

Industry/Entity Type

Business

Requirements
Must have
• - must fit the look and feel of the logo (notice that I have attached the logo, and an emblem)
- the final files should be ready for printing - with info on colours, sizes, bleed area, margins, UV spot (if applicable), suggested material to print on (applies to business cards in particular)
- brand guide lines should be laid out too (font, colour, etc ...)
Nice to have
• It would be nice to produce something different that your standard sizes & di-cut in terms of business card, and letter head ...
Should not have
• THE EMBLEM (MD) AND THE LOGO (MARK DELOURIS) SHOULD NOT BE LAYED OUT AS PER THE ATTACHED FILE - THEY SHOULD BE SEPARATED - THE EMBLEM (MD) CAN BE USED IN PARTIAL OR AS WATERMARK - BUT NOT THE LOGO (MARK DELOURIS)

```html
<!DOCTYPE html>
<html lang="en">
<head>
<meta charset="utf-8">
<title>Mark Delouris — Envelope Stationery</title>
<link href="https://fonts.googleapis.com/css2?family=Oswald:wght@600&family=Open+Sans:wght@400;600&display=swap" rel="stylesheet">
<style>
  :root {
    --backdrop: #e4e5e6;
    --paper: #f7f7f7;
    --paper-edge: #dcdddf;
    --brand-blue: #4fa9d2;
    --ink: #55585c;
    --ink-soft: #7a7d81;
    --watermark: #e6e7e8;
    --emblem-grey: #5e6064;
  }
  * { box-sizing: border-box; margin: 0; padding: 0; }
  html, body { width: 1200px; height: 795px; overflow: hidden; }
  body {
    background: var(--backdrop);
    font-family: "Open Sans", sans-serif;
    position: relative;
  }
  .envelope {
    position: absolute;
    width: 520px;
    height: 260px;
    background: var(--paper);
    box-shadow: 0 2px 0 var(--paper-edge), 0 10px 24px rgba(0,0,0,0.08);
    overflow: hidden;
  }
  .envelope--front { left: 50px; top: 268px; }
  .envelope--back { left: 630px; top: 268px; }

  .envelope__art { position: absolute; inset: 0; width: 100%; height: 100%; }

  .sender {
    position: absolute;
    left: 24px;
    top: 22px;
    width: 210px;
  }
  .sender__name {
    font-family: "Oswald", sans-serif;
    font-weight: 600;
    font-size: 27px;
    line-height: 1;
    letter-spacing: 0.5px;
    color: var(--ink);
  }
  .sender__rule {
    height: 1.5px;
    background: var(--brand-blue);
    margin: 3px 0 2px;
  }
  .sender__tagline {
    font-size: 6px;
    color: var(--brand-blue);
    text-align: right;
    margin-bottom: 5px;
  }
  .sender__contact {
    list-style: none;
    font-size: 6.5px;
    line-height: 1.45;
    color: var(--ink);
  }
  .sender__contact li { display: flex; align-items: center; gap: 4px; }
  .sender__icon { width: 6px; height: 6px; flex: none; }

  .band-url {
    font-family: "Open Sans", sans-serif;
    font-size: 11px;
    fill: #3b86ab;
  }
</style>
</head>
<body>

  <section class="envelope envelope--front" aria-label="Envelope front">
    <svg class="envelope__art" viewBox="0 0 520 260" aria-hidden="false">
      <circle class="watermark-emblem" cx="430" cy="205" r="72" fill="none" stroke="var(--watermark)" stroke-width="10"/>
      <path class="brand-band" d="M0,168 Q270,236 520,248 L520,260 L0,260 Z" fill="var(--brand-blue)"/>
      <path class="brand-band__shade" d="M0,190 Q260,252 520,260 L0,260 Z" fill="#ffffff" opacity="0"/>
      <path id="band-line" d="M120,214 Q270,238 420,250" fill="none"/>
      <text class="band-url"><textPath href="#band-line" startOffset="50%" text-anchor="middle">markdelouris.net</textPath></text>
    </svg>

    <div class="sender">
      <div class="sender__name">MARK DELOURIS</div>
      <div class="sender__rule"></div>
      <div class="sender__tagline">Executive coaching and public speaking</div>
      <ul class="sender__contact">
        <li>
          <svg class="sender__icon" viewBox="0 0 10 10"><path d="M2 1 L4 1 L5 3 L4 4 Q5 6 6 6 L7 5 L9 6 L9 8 Q5 9 2 5 Q1 3 2 1 Z" fill="var(--brand-blue)"/></svg>
          00961 70 318527
        </li>
        <li>
          <svg class="sender__icon" viewBox="0 0 10 10"><rect x="0.5" y="2" width="9" height="6" fill="none" stroke="var(--brand-blue)" stroke-width="1.2"/><path d="M0.5 2 L5 6 L9.5 2" fill="none" stroke="var(--brand-blue)" stroke-width="1.2"/></svg>
          me@markdelouris.net
        </li>
        <li>Harbor City - Corvania, P.O.Box 41-208 Westmere</li>
      </ul>
    </div>
  </section>

  <section class="envelope envelope--back" aria-label="Envelope back">
    <svg class="envelope__art" viewBox="0 0 520 260">
      <path class="flap-edge" d="M12,0 L12,92 Q12,100 20,100 L500,100 Q508,100 508,92 L508,0" fill="none" stroke="#e2e3e4" stroke-width="1.5"/>
      <circle class="seal-emblem" cx="260" cy="100" r="22" fill="var(--emblem-grey)"/>
    </svg>
  </section>

</body>
</html>
```